Pelican Litigation Funding Letterhead & Document Template

We need a letter head designed for our fund. Our fund works with law firms and investors across the globe. We need a a cover letter template as well as a document template for subsequent pages. Blue and white color scheme is preferred. This is our predecessor's website: https://www.pelicanvq.com/index.html. Please see our logo attached. The logo color code is #19478d. Font is Gotham-Medium.
Target Market(s)
Sophisticated investors and law firms
Font styles to use
Sans Serif
Colors
0255a3

```html
<!DOCTYPE html>
<html lang="en">
<head>
<meta charset="utf-8">
<title>Pelican Litigation Funding Letterhead</title>
<link rel="stylesheet" href="https://fonts.googleapis.com/css2?family=Open+Sans:wght@400;600&display=swap">
<style>
  :root {
    --brand-blue: #19478d;
    --ink: #4a4a4a;
    --ink-soft: #5c5c5c;
    --rule: #b8b8b8;
    --paper: #ffffff;
    --backdrop: #e4e4e6;
  }
  * { margin: 0; padding: 0; box-sizing: border-box; }
  html, body {
    width: 1063px; height: 1200px; overflow: hidden;
    background: var(--backdrop);
  }
  .letterhead {
    position: absolute; left: 76px; top: 40px;
    width: 911px; height: 1120px;
    background: var(--paper);
    box-shadow: 0 2px 10px rgba(0,0,0,0.12);
    font-family: "Open Sans", Arial, sans-serif;
    color: var(--ink);
  }
  .brand {
    position: absolute; left: 80px; top: 130px;
    display: flex; align-items: center; gap: 12px;
  }
  .brand-square { width: 26px; height: 26px; background: var(--brand-blue); }
  .brand-name {
    font-weight: 600; font-size: 22px; letter-spacing: 0.5px;
    color: var(--brand-blue); text-transform: uppercase;
  }
  .contact {
    position: absolute; left: 560px; top: 70px;
    padding-left: 26px; border-left: 1px solid var(--rule);
    font-size: 13.5px; line-height: 19px; color: var(--ink);
  }
  .contact-address { margin-bottom: 6px; }
  .contact-line { display: flex; align-items: center; gap: 8px; }
  .contact-line svg { width: 12px; height: 12px; fill: var(--brand-blue); flex: none; }
  .letter-body {
    position: absolute; left: 80px; top: 300px; width: 740px;
    font-size: 14.5px; line-height: 22px; color: var(--ink-soft);
  }
  .salutation { margin-bottom: 14px; }
  .letter-body p.paragraph { margin-bottom: 22px; }
  .closing { margin-top: 10px; }
  .signature-area {
    margin-top: 22px; width: 150px; height: 70px;
    background: linear-gradient(90deg, #f2f2f2, #e6e6e6);
  }
</style>
</head>
<body>
  <main class="letterhead">
    <header>
      <div class="brand">
        <span class="brand-square"></span>
        <span class="brand-name">Pelican Litigation Funding</span>
      </div>
      <address class="contact" style="font-style:normal">
        <div class="contact-address">Marlow Court - Upper Floor<br>4180 Harbor Lane, Suite 920<br>Dallas, Texas 75201</div>
        <div class="contact-line"><svg viewBox="0 0 24 24"><path d="M6.6 10.8a15 15 0 0 0 6.6 6.6l2.2-2.2a1 1 0 0 1 1-.25 11.4 11.4 0 0 0 3.6.57 1 1 0 0 1 1 1V20a1 1 0 0 1-1 1A17 17 0 0 1 3 4a1 1 0 0 1 1-1h3.5a1 1 0 0 1 1 1c0 1.25.2 2.45.57 3.57a1 1 0 0 1-.25 1z"/></svg>(555) 402-3100</div>
        <div class="contact-line"><svg viewBox="0 0 24 24"><path d="M6 3h12v5H6zM4 9h16a2 2 0 0 1 2 2v6h-4v4H6v-4H2v-6a2 2 0 0 1 2-2zm4 7v3h8v-3z"/></svg>(555) 402-3200</div>
        <div class="contact-line"><svg viewBox="0 0 24 24"><path d="M2 5h20v14H2zm2 2v.5l8 5 8-5V7zm0 2.8V17h16V9.8l-8 5z"/></svg>info@pelicanvq.com</div>
        <div class="contact-line"><svg viewBox="0 0 24 24"><circle cx="12" cy="12" r="10"/></svg>www.pelicanvq.com</div>
      </address>
    </header>
    <section class="letter-body">
      <p class="salutation">Dear customer,</p>
      <p class="paragraph">Lorem ipsum dolor sit amet, consectetur adipisicing elit, sed do eiusmod tempor incididunt ut labore et dolore magna aliqua. Ut enim ad minim veniam, quis nostrud exercitation ullamco laboris nisi ut aliquip ex ea commodo consequat. Duis aute irure dolor in reprehenderit in voluptate velit esse cillum dolore eu fugiat nulla pariatur. Excepteur sint occaecat cupidatat non proident, sunt in culpa qui officia deserunt mollit anim id est laborum.</p>
      <p class="paragraph">Lorem ipsum dolor sit amet, consectetur adipisicing elit, sed do eiusmod tempor incididunt ut labore et dolore magna aliqua. Ut enim ad minim veniam, quis nostrud exercitation ullamco laboris nisi ut aliquip ex ea commodo consequat. Duis aute irure dolor in reprehenderit in voluptate velit esse cillum dolore eu fugiat nulla pariatur. Excepteur sint occaecat cupidatat non proident, sunt in culpa qui officia deserunt mollit anim id est laborum.</p>
      <p class="paragraph">Lorem ipsum dolor sit amet, consectetur adipisicing elit, sed do eiusmod tempor incididunt ut labore et dolore magna aliqua. Ut enim ad minim veniam, quis nostrud exercitation ullamco laboris nisi ut aliquip ex ea commodo consequat. Duis aute irure dolor in reprehenderit in voluptate velit esse cillum dolore eu fugiat nulla pariatur. Excepteur sint occaecat cupidatat non proident, sunt in culpa qui officia deserunt mollit anim id est laborum.</p>
      <p class="paragraph">Lorem ipsum dolor sit amet, consectetur adipisicing elit, sed do eiusmod tempor incididunt ut labore et dolore magna aliqua. Ut enim ad minim veniam, quis nostrud exercitation ullamco laboris nisi ut aliquip ex ea commodo consequat. Duis aute irure dolor in reprehenderit.</p>
      <p class="closing">Yours Sincerely,</p>
      <div class="signature-area" role="img" aria-label="Handwritten signature of the sender"></div>
    </section>
  </main>
</body>
</html>
```